Silver Heron Coffee Bean Labels

We need a label for a new brand of coffee that we are selling in Portland, Oregon (Coffee Capital). Our company has no current online presence but have some great roasting techniques. We will be roasting our own coffee beans from throughout the world and selling them immediately after roasting causing a super fresh and high quality product.

We will be packaging in brown kraft bags: 3 3/8 X 2.5 x 7.75 inches which is standard for coffee beans.

Also notice on that sample the blue section in the middle has the product name. We want to also make it so that there is a consistent area that we can print OVER the label the name or blend of the coffee.

Our company is called Silver Heron Coffee Roasters. We will want to put silverheronroasters.example on the label someplace (we dont have a site yet but will by launch).

We need to incorporate A Silver Heron into the design. No preferences yet on the style of it.

We want to be a super-premium brand. Sort of like MicroBrew beers. We will sell at Farmers Markets, online, and directly into stores. Image is very important to us.

Labels should be about 3" wide and about 3.75" high.. Perhaps higher if a cool design justifies the height. Again we will be using a brown kraft bag (like grocery bag color) as shown on the sample.

SEE ATTACHED SEVERAL INTERESTING DESIGNS

Target Market(s)

Foodies, Yuppie, Coffee Snob

Industry/Entity Type

It Company

Requirements
Must have
• Location for the product Name to go onto it... We want to use the same labels for our full line. Just printing over it something like "Italian Roast" and a line below saying something like "Bold, Nutty Flavor, blah blah"

Should not have
• Clunkey looking old fonts or things that look homemade.

```html
<!DOCTYPE html>
<html lang="en">
<head>
<meta charset="utf-8">
<title>Silver Heron Coffee Roasters – Bean Label</title>
<link href="https://fonts.googleapis.com/css2?family=Oswald:wght@500;600&family=Rokkitt:wght@700&family=Archivo+Narrow:wght@500&display=swap" rel="stylesheet">
<style>
  :root {
    --backdrop: #c9a477;
    --label-yellow: #f1b935;
    --label-charcoal: #3d3b3a;
    --brand-grey: #9a9794;
    --ink-dark: #26221f;
    --rule-grey: #7e7b78;
  }
  html, body {
    margin: 0;
    padding: 0;
    width: 1200px;
    height: 1000px;
    overflow: hidden;
    background: var(--backdrop);
  }
  .label {
    position: absolute;
    left: 302px;
    top: 60px;
    width: 596px;
    height: 880px;
    display: flex;
    flex-direction: column;
    box-shadow: 0 6px 24px rgba(0,0,0,0.25);
  }
  .roast-level {
    height: 51px;
    background: var(--label-yellow);
    display: flex;
    align-items: center;
    justify-content: center;
    font-family: 'Rokkitt', serif;
    font-weight: 700;
    font-size: 30px;
    letter-spacing: 3px;
    color: var(--ink-dark);
  }
  .masthead {
    height: 309px;
    background: var(--label-charcoal);
    display: flex;
    flex-direction: column;
    align-items: center;
    justify-content: center;
    font-family: 'Oswald', sans-serif;
    font-weight: 600;
    color: var(--brand-grey);
    text-transform: uppercase;
    line-height: 1;
  }
  .masthead .name-top { font-size: 88px; letter-spacing: 14px; }
  .masthead .name-main { font-size: 110px; letter-spacing: 4px; margin-top: 2px; }
  .masthead .name-sub { font-size: 40px; letter-spacing: 9px; margin-top: 8px; }
  .since {
    display: flex;
    align-items: center;
    gap: 18px;
    margin-top: 14px;
    font-family: 'Oswald', sans-serif;
    font-weight: 500;
    font-size: 26px;
    letter-spacing: 3px;
    color: var(--brand-grey);
  }
  .since::before, .since::after {
    content: "";
    width: 120px;
    height: 2px;
    background: var(--rule-grey);
  }
  .blend-band {
    height: 90px;
    background: var(--label-yellow);
    display: flex;
    flex-direction: column;
    align-items: center;
    justify-content: center;
    color: var(--ink-dark);
  }
  .blend-name {
    font-family: 'Oswald', sans-serif;
    font-weight: 600;
    font-size: 44px;
    line-height: 1;
  }
  .blend-notes {
    font-family: 'Archivo Narrow', sans-serif;
    font-weight: 500;
    font-size: 15px;
    margin-top: 10px;
  }
  .footer {
    flex: 1;
    background: var(--label-charcoal);
    display: flex;
    flex-direction: column;
    align-items: center;
    padding: 0 40px;
  }
  .footer-brand {
    margin-top: 128px;
    display: flex;
    align-items: center;
    gap: 18px;
    font-family: 'Oswald', sans-serif;
    font-weight: 600;
    font-size: 38px;
    letter-spacing: 3px;
    text-transform: uppercase;
    color: var(--brand-grey);
  }
  .footer-brand .mark {
    width: 40px;
    height: 40px;
    border-radius: 50%;
    border: 3px solid var(--brand-grey);
    box-sizing: border-box;
  }
  .story {
    margin: 38px 0 0;
    font-family: 'Archivo Narrow', sans-serif;
    font-weight: 500;
    font-size: 17px;
    line-height: 1.4;
    color: var(--brand-grey);
    text-align: center;
  }
  .web-address {
    margin-top: 42px;
    font-family: 'Rokkitt', serif;
    font-weight: 700;
    font-size: 26px;
    letter-spacing: 3px;
    text-transform: uppercase;
    color: var(--brand-grey);
  }
</style>
</head>
<body>
  <main class="label">
    <div class="roast-level">MEDIUM ROAST</div>
    <header class="masthead">
      <div class="name-top">Silver</div>
      <div class="name-main">Heron</div>
      <div class="name-sub">Coffee Roasters</div>
      <div class="since">SINCE 2013</div>
    </header>
    <section class="blend-band">
      <div class="blend-name">Italian Roast</div>
      <div class="blend-notes">A robust coffee with a bold, nutty flavor etc...</div>
    </section>
    <footer class="footer">
      <div class="footer-brand"><span class="mark"></span>Silver Heron Coffee Roasters</div>
      <p class="story">Silver Heron Coffee Roasters source only the finest coffee beans from farms around the world, roasted in small batches for the highest quality and flavor.</p>
      <div class="web-address">silverheronroasters.example</div>
    </footer>
  </main>
</body>
</html>
```